Business cards and stationary for Auto Body Shop
R & T Auto Body Service Inc.
Simple
Delmor Quenivash
28476 Pellway Street
Corvell Bay, CA 95555
rtautobodyinc@brivomail.com
www.rtautobody-example.com
Just the Logo I guess.
Please us this new logo.

```html
<!DOCTYPE html>
<html lang="en">
<head>
<meta charset="utf-8">
<title>Auto Body Business Card</title>
<link href="https://fonts.googleapis.com/css2?family=Cinzel:wght@400;600&display=swap" rel="stylesheet">
<style>
  :root {
    --page: #d9d9db;
    --card: #ffffff;
    --ink: #2a2a2c;
    --ink-soft: #6b6b6e;
    --band-dark: #3a3a3c;
    --band-mid: #8c8c90;
    --shadow: rgba(0,0,0,0.18);
  }
  * { box-sizing: border-box; margin: 0; padding: 0; }
  html, body { width: 1200px; height: 864px; overflow: hidden; }
  body {
    background: var(--page);
    font-family: "Cinzel", "Times New Roman", serif;
    color: var(--ink);
    position: relative;
  }
  .card {
    position: absolute;
    top: 278px;
    width: 540px;
    height: 308px;
    background: var(--card);
    border-radius: 22px;
    box-shadow: 0 10px 28px var(--shadow);
    overflow: hidden;
  }
  .card--front { left: 40px; }
  .card--back { left: 620px; }

  /* Front */
  .front-mark {
    position: absolute;
    left: 0; right: 0; top: 96px;
    text-align: center;
    font-size: 64px;
    font-weight: 600;
    letter-spacing: 2px;
    color: var(--ink);
  }
  .front-url {
    position: absolute;
    left: 0; right: 0; top: 206px;
    text-align: center;
    font-size: 11px;
    letter-spacing: 5px;
    text-transform: uppercase;
    color: var(--ink-soft);
  }

  /* Back */
  .wave { position: absolute; right: 0; top: 0; width: 150px; height: 308px; }
  .brand {
    position: absolute;
    left: 30px; top: 46px;
    display: flex; align-items: center; gap: 14px;
  }
  .brand-circle {
    width: 78px; height: 78px;
    border-radius: 50%;
    border: 5px solid var(--ink);
    flex: none;
  }
  .brand-name {
    font-size: 30px;
    font-weight: 600;
    color: var(--ink);
    letter-spacing: 1px;
    white-space: nowrap;
  }
  .owner {
    position: absolute;
    left: 34px; top: 176px;
    font-size: 14px;
    letter-spacing: 1px;
    white-space: nowrap;
  }
  .address {
    position: absolute;
    left: 34px; top: 212px;
    font-size: 10.5px;
    line-height: 1.6;
    color: var(--ink-soft);
    letter-spacing: .5px;
    white-space: nowrap;
  }
  .contacts {
    position: absolute;
    left: 248px; top: 142px;
    list-style: none;
    font-size: 9.5px;
    line-height: 19px;
    color: var(--ink-soft);
  }
  .contacts li { display: flex; align-items: center; gap: 7px; white-space: nowrap; }
  .contacts .icon {
    width: 12px; height: 12px; flex: none;
    border-radius: 50%;
    background: var(--ink);
    display: flex; align-items: center; justify-content: center;
  }
  .contacts .icon svg { width: 8px; height: 8px; }
</style>
</head>
<body>
  <section class="card card--front" aria-label="Business card front">
    <div class="front-mark">R &amp; T</div>
    <p class="front-url">www.rtautobody-example.com</p>
  </section>

  <section class="card card--back" aria-label="Business card back">
    <svg class="wave" viewBox="0 0 150 308" preserveAspectRatio="none" aria-hidden="true">
      <path d="M150 0 L118 0 C60 60 150 130 90 200 C60 240 70 280 60 308 L150 308 Z" fill="var(--band-mid)"/>
      <path d="M150 0 L132 0 C80 60 160 130 104 200 C76 240 84 280 78 308 L150 308 Z" fill="var(--band-dark)"/>
    </svg>

    <div class="brand">
      <div class="brand-circle"></div>
      <div class="brand-name">R &amp; T AUTO BODY</div>
    </div>

    <p class="owner">Delmor Quenivash</p>
    <p class="address">28476 Pellway Street<br>Corvell Bay, CA 95555</p>

    <ul class="contacts">
      <li><span class="icon"><svg viewBox="0 0 10 10"><path d="M2 1 L4 1 L4.6 3 L3.4 3.8 C4 5.2 4.8 6 6.2 6.6 L7 5.4 L9 6 L9 8 C5 8.5 1.5 5 2 1 Z" fill="#fff"/></svg></span>818-555-0147</li>
      <li><span class="icon"><svg viewBox="0 0 10 10"><path d="M2 1 L4 1 L4.6 3 L3.4 3.8 C4 5.2 4.8 6 6.2 6.6 L7 5.4 L9 6 L9 8 C5 8.5 1.5 5 2 1 Z" fill="#fff"/></svg></span>818-555-0162</li>
      <li><span class="icon"><svg viewBox="0 0 10 10"><rect x="2" y="3" width="6" height="4" fill="#fff"/><rect x="3" y="1.5" width="4" height="1.5" fill="#fff"/></svg></span>818-555-0188</li>
      <li><span class="icon"><svg viewBox="0 0 10 10"><rect x="1.5" y="2.5" width="7" height="5" fill="#fff"/><path d="M1.5 2.5 L5 5.5 L8.5 2.5" stroke="#2a2a2c" stroke-width="0.8" fill="none"/></svg></span>rtautobodyinc@brivomail.com</li>
      <li><span class="icon"><svg viewBox="0 0 10 10"><circle cx="5" cy="5" r="3.4" stroke="#fff" stroke-width="1" fill="none"/><path d="M1.6 5 H8.4" stroke="#fff" stroke-width="0.8"/></svg></span>www.rtautobody-example.com</li>
      <li><span class="icon"></span>R_T_Auto_Body</li>
    </ul>
  </section>
</body>
</html>
```